Criação de Layout Web-Design para Beleza
" Nossa empresa promove o embelezamento de nossos clientes com protocolos exclusivos adequados a cada cliente respeitando sempre suas singularidades. "

```html
<!DOCTYPE html>
<html lang="pt-BR">
<head>
<meta charset="UTF-8">
<title>Agende uma Consultoria Estética</title>
<link rel="stylesheet" href="https://fonts.googleapis.com/css2?family=Open+Sans:wght@300;400;600&display=swap">
<style>
  :root {
    --canvas-bg: #ecebee;
    --header-top: #8a5fb8;
    --header-bottom: #5b3a8c;
    --header-dot: #2e1f44;
    --hero-light: #fbf7f6;
    --hero-skin: #f1dcd6;
    --hero-rose: #e9c3c7;
    --figure-skin: #d9a98c;
    --figure-light: #f4ece8;
    --accent-purple: #b27fd6;
    --title-dark: #4a4a4f;
    --label-grey: #6d6b70;
    --field-border: #b08fd0;
    --field-bg: #ffffff;
    --button-bg: #f28c99;
    --button-text: #ffffff;
  }
  * { margin: 0; padding: 0; box-sizing: border-box; }
  html, body {
    width: 1200px; height: 1200px; overflow: hidden;
    background: var(--canvas-bg);
    font-family: "Open Sans", Arial, sans-serif;
  }
  .landing-page {
    position: absolute; left: 40px; top: 200px;
    width: 1120px; height: 800px; overflow: hidden;
    background: var(--hero-light);
    box-shadow: 0 10px 40px rgba(0,0,0,0.12);
  }
  .top-bar {
    position: absolute; left: 0; top: 0; width: 100%; height: 115px;
    background: linear-gradient(180deg, var(--header-top), var(--header-bottom));
    z-index: 2;
  }
  .top-bar .dots { position: absolute; top: 50px; display: flex; gap: 12px; }
  .top-bar .dots.left { left: 70px; }
  .top-bar .dots.center { left: 560px; }
  .top-bar .dots span {
    width: 10px; height: 10px; border-radius: 50%; background: var(--header-dot);
  }
  .hero-backdrop {
    position: absolute; left: 0; top: 115px; width: 100%; height: 685px;
    background:
      radial-gradient(ellipse 420px 340px at 640px 200px, var(--hero-skin), transparent 70%),
      radial-gradient(ellipse 220px 160px at 560px 500px, var(--hero-rose), transparent 70%),
      linear-gradient(90deg, var(--hero-light), #f6ecea 50%, var(--hero-light));
  }
  .model-photo {
    position: absolute; left: 30px; top: 300px; width: 460px; height: 460px;
    border-radius: 40% 40% 10px 10px;
    background: linear-gradient(160deg, var(--figure-light) 0%, var(--figure-skin) 55%, var(--figure-light) 100%);
    opacity: 0.85;
  }
  .booking-form {
    position: absolute; left: 580px; top: 250px; width: 470px; z-index: 3;
  }
  .booking-form .kicker {
    font-weight: 300; font-size: 40px; line-height: 1.1; color: var(--accent-purple);
  }
  .booking-form h1 {
    font-weight: 400; font-size: 42px; line-height: 1.2; color: var(--title-dark);
    margin-bottom: 18px;
  }
  .field { margin-bottom: 16px; }
  .field label {
    display: block; font-size: 17px; color: var(--label-grey); margin-bottom: 4px;
  }
  .field .input {
    height: 54px; border: 2px solid var(--field-border); background: var(--field-bg);
  }
  .submit-button {
    margin-top: 14px; height: 56px; background: var(--button-bg);
    color: var(--button-text); font-weight: 600; font-size: 19px; letter-spacing: 1px;
    display: flex; align-items: center; justify-content: center;
  }
</style>
</head>
<body>
  <main class="landing-page">
    <header class="top-bar">
      <div class="dots left"><span></span><span></span><span></span><span></span><span></span></div>
      <div class="dots center"><span></span><span></span><span></span><span></span><span></span></div>
    </header>

    <div class="hero-backdrop" role="img" aria-label="Close-up photograph of a woman's face and hand with pink nails, soft background"></div>
    <div class="model-photo" role="img" aria-label="Photograph of a woman in white clothing sitting on the floor"></div>

    <form class="booking-form">
      <p class="kicker">Agende uma</p>
      <h1>Consultoria Estética</h1>
      <div class="field"><label>Nome</label><div class="input"></div></div>
      <div class="field"><label>E-mail</label><div class="input"></div></div>
      <div class="field"><label>DDD+Telefone</label><div class="input"></div></div>
      <div class="submit-button">SOLICITAR AGENDAMENTO</div>
    </form>
  </main>
</body>
</html>
```